Website for an electrical contractor :)

We are after a web site which can show pictures of our jobs and our capability in a professional, creative and easily understood way.

----- Brightvale Electrical ------

We really want a visually good looking website with three sections

Section one:
'Completed projects'
We have a few pictures of jobs which we've completed and would like to show off with a brief description. (see uploads)

Section two:
'Our capabilities'
Just a list of what services we offer

Section three:
We would like a 'contact us' section which people can send us a short msg and upload a file for plans to be able to send to us. We would need their name, phone number and email details. We would also need a short privacy policy saying 'we do not disclose information to third parties'.
We also want to display our contact number and postal address

Good luck :)

Target Market(s)

Adults 25 years+
Business owners
Builders
Real estate agents

Industry/Entity Type

Electrical

Colors

Designer to choose colors to be used in the design.

Requirements
Must have
• Visually appealing
Easy to understand
In the 'Completed projects' section, must have a list for each project we do i can upload pictures for it.

```html
<!DOCTYPE html>
<html lang="en">
<head>
<meta charset="utf-8">
<title>Brightvale Electrical &amp; Communications</title>
<link href="https://fonts.googleapis.com/css2?family=Roboto:wght@300;400;500;700&family=Open+Sans:wght@400;700&display=swap" rel="stylesheet">
<style>
:root{
  --red:#e21f26;
  --dark:#2b2829;
  --darker:#222021;
  --ink:#1c1a1b;
  --grey:#8a8788;
  --white:#ffffff;
  --line:#9a9798;
}
*{margin:0;padding:0;box-sizing:border-box}
html,body{width:674px;height:1200px;overflow:hidden;background:var(--white)}
body{position:relative;font-family:'Roboto',sans-serif;color:var(--white)}
.abs{position:absolute}

/* header */
.site-header{left:0;top:0;width:674px;height:37px;background:var(--dark);border-bottom:2px solid var(--red)}
.brand-tab{left:152px;top:0;width:25px;height:42px;background:var(--white);clip-path:polygon(0 0,100% 0,100% 80%,50% 100%,0 80%)}
.brand-dot{left:159px;top:12px;width:11px;height:11px;border-radius:50%;background:var(--red)}
.brand-name{left:180px;top:7px;font-size:15px;font-weight:300;color:#c9c7c8;letter-spacing:-.2px}
.topbar{left:310px;top:0;width:210px;height:11px;background:#3a3738;font-size:4.6px;line-height:11px;text-align:center;color:#ddd}
.topbar b{color:var(--red);font-weight:500}
.main-nav{left:314px;top:19px;display:flex;gap:0;font-size:6.2px;color:var(--white)}
.main-nav span{padding:0 9px;border-left:1px solid #ccc;line-height:7px}
.main-nav span:first-child{border-left:none;color:var(--red)}

/* hero */
.hero{left:0;top:39px;width:674px;height:191px;background:linear-gradient(100deg,#4e4a48 0%,#8d8884 40%,#6b6764 70%,#3e3b3a 100%)}
.hero-title{left:194px;top:98px;font-size:14px;font-weight:700;line-height:15px;letter-spacing:-.3px;text-transform:uppercase}
.hero-title .red{color:var(--red)}
.hero-text{left:194px;top:130px;width:140px;font-size:6.2px;line-height:7.5px}
.hero-btn{left:194px;top:155px;width:48px;height:14px;background:var(--red);font-size:5.6px;font-weight:700;line-height:14px;text-align:center;border-radius:2px}
.hero-arrow{top:120px}
.hero-dots{left:326px;top:215px;display:flex;gap:3px}
.hero-dots i{width:4px;height:4px;border-radius:50%;background:var(--white)}
.hero-dots i.on{background:var(--red);box-shadow:0 0 0 1px #fff}

/* welcome */
.welcome-title{left:0;top:251px;width:674px;text-align:center;font-size:12.5px;color:var(--ink)}
.welcome-title span{color:var(--red)}
.welcome-col{top:281px;font-size:4.6px;line-height:8.4px;color:#333}

/* projects */
.projects{left:0;top:352px;width:674px;height:254px;background:var(--dark)}
.section-title{left:0;width:674px;text-align:center;font-size:16px;font-weight:400}
.section-sub{left:0;width:674px;text-align:center;font-size:6px;letter-spacing:5px;color:var(--red)}
.shot{height:95px}

/* capabilities */
.capabilities{left:0;top:606px;width:674px;height:242px;background:linear-gradient(180deg,#3b3839 0%,#4a4647 35%,#2e2b2c 100%)}
.cap-head{top:702px;font-size:10px;font-weight:400}
.cap-list{top:725px;width:86px;list-style:none;font-size:4.8px}
.cap-list li{height:10.7px;line-height:9.5px;border-bottom:1px solid var(--line)}

/* contact */
.contact{left:0;top:848px;width:674px;height:316px;background:var(--darker)}
.field{height:16px;background:var(--white);font-size:4.8px;color:#777;padding:0 6px;line-height:16px;text-transform:uppercase}
.btn-red{background:var(--red);color:var(--white);font-size:5.5px;font-weight:700;text-align:center;border-radius:2px;text-transform:uppercase}
.info{top:1091px;width:110px;text-align:center;font-family:'Open Sans',sans-serif}
.info h4{font-size:7.5px;font-weight:700;margin:5px 0 3px}
.info p{font-size:6px;line-height:7px;color:#e6e6e6}

/* footer */
.site-footer{left:0;top:1164px;width:674px;height:36px;background:var(--white);font-size:4.6px;color:#333}
</style>
</head>
<body>

<header>
  <div class="abs site-header"></div>
  <div class="abs brand-tab"></div>
  <div class="abs brand-dot"></div>
  <div class="abs brand-name">Brightvale</div>
  <div class="abs topbar"><b>E:</b> info@brightvaleelectrical.com.au &nbsp;&nbsp; <b>P:</b> 0400 318 562 &nbsp;&nbsp; <b>A.B.N</b> 48 219 630 775</div>
  <nav class="abs main-nav"><span>Home</span><span>Complete Projects</span><span>Our capabilities</span><span>Contact Us</span></nav>
</header>

<section>
  <div class="abs hero" role="img" aria-label="Photo of a finished interior fit-out with lounge seating and ceiling downlights"></div>
  <h1 class="abs hero-title"><span class="red">Brightvale Electrical</span><br>&amp; Communications</h1>
  <p class="abs hero-text">Lorem Ipsum is simply dummy text of the printing and typesetting industry.</p>
  <div class="abs hero-btn">READ MORE</div>
  <svg class="abs hero-arrow" style="left:150px" width="16" height="26" viewBox="0 0 16 26"><path d="M14 1 2 13l12 12" fill="none" stroke="#fff" stroke-width="1.3"/></svg>
  <svg class="abs hero-arrow" style="left:508px" width="16" height="26" viewBox="0 0 16 26"><path d="M2 1l12 12L2 25" fill="none" stroke="#fff" stroke-width="1.3"/></svg>
  <div class="abs hero-dots"><i></i><i class="on"></i><i></i><i></i></div>
</section>

<section>
  <h2 class="abs welcome-title">Welcome to <span>Brightvale Electrical &amp; Communications.</span></h2>
  <p class="abs welcome-col" style="left:152px;width:170px">Lorem Ipsum is simply dummy text of the printing and typesetting industry. Lorem Ipsum has been the industry's standard dummy text ever since the 1500s, when an unknown printer took a galley of type and scrambled it to make a type specimen book. It has survived not only five centuries, but also the leap into electronic typesetting, remaining essentially unchanged.</p>
  <p class="abs welcome-col" style="left:342px;width:182px">It was popularised in the 1960s with the release of Letraset sheets containing Lorem Ipsum passages, and more recently with desktop publishing software like Aldus PageMaker including versions of Lorem Ipsum.</p>
</section>

<section>
  <div class="abs projects"></div>
  <h2 class="abs section-title" style="top:370px">Completed Projects</h2>
  <div class="abs section-sub" style="top:391px">PORTFOLIO</div>

  <div class="abs shot" style="left:0;top:415px;width:9px;background:#8a8684" role="img" aria-label="Project photo edge"></div>
  <div class="abs shot" style="left:10px;top:415px;width:130px;background:linear-gradient(#c9c6c2,#6d6966)" role="img" aria-label="Office interior with ceiling lights"></div>
  <div class="abs shot" style="left:141px;top:415px;width:130px;background:linear-gradient(#a9c2d8,#b8b2a8 55%,#8d8a86)" role="img" aria-label="Residential driveway with garden beds"></div>
  <div class="abs shot" style="left:272px;top:415px;width:130px;background:linear-gradient(#dcdad6,#7c7876)" role="img" aria-label="Commercial interior with large windows"></div>
  <div class="abs shot" style="left:403px;top:415px;width:129px;background:linear-gradient(#4f86c8,#bcb6a8 55%,#9a958c)" role="img" aria-label="New townhouse exterior under blue sky"></div>
  <div class="abs shot" style="left:533px;top:415px;width:130px;background:linear-gradient(#d8d8d6,#6d6b68 55%,#a49a86)" role="img" aria-label="Warehouse frame with elevated work platform"></div>
  <div class="abs shot" style="left:664px;top:415px;width:10px;background:#8a8684" role="img" aria-label="Project photo edge"></div>

  <div class="abs shot" style="left:0;top:511px;width:9px;background:#8a8684" role="img" aria-label="Project photo edge"></div>
  <div class="abs shot" style="left:10px;top:511px;width:130px;background:linear-gradient(#dcdcda,#5f5c5a 55%,#9a907e)" role="img" aria-label="Open shed under construction"></div>
  <div class="abs shot" style="left:141px;top:511px;width:130px;background:linear-gradient(#9fb6c9,#6f5a48 40%,#5b4636)" role="img" aria-label="Slab reinforcement mesh on site"></div>
  <div class="abs shot" style="left:272px;top:511px;width:130px;background:linear-gradient(#5b8fcf,#c9c9c7 50%,#9a9690)" role="img" aria-label="Concrete commercial building exterior"></div>
  <div class="abs shot" style="left:403px;top:511px;width:129px;background:linear-gradient(#8f8878,#d6d2c8 50%,#8a8270)" role="img" aria-label="Company site sign on a construction fence"></div>
  <div class="abs shot" style="left:533px;top:511px;width:130px;background:linear-gradient(90deg,#b8242a,#d9d6d2 50%,#b8242a)" role="img" aria-label="Rows of switchboard breakers"></div>
  <div class="abs shot" style="left:664px;top:511px;width:10px;background:#8a8684" role="img" aria-label="Project photo edge"></div>
</section>

<section>
  <div class="abs capabilities" role="img" aria-label="Darkened photo of a building site behind the capabilities list"></div>
  <div class="abs section-sub" style="top:653px;color:#fff;font-size:7px;letter-spacing:5px">OUR CAPABILITIES</div>
  <h3 class="abs cap-head" style="left:150px">Residential</h3>
  <h3 class="abs cap-head" style="left:342px">Commercial / Industrial</h3>
  <ul class="abs cap-list" style="left:150px"><li>24hr Support / faults</li><li>RCD (Safety Switch) installations</li><li>Smoke alarms</li><li>Power points</li><li>Lighting points</li><li>External lighting</li><li>Sensor lighting</li><li>Switching</li><li>Antennas and Arial points</li><li>Dimmers</li><li>Ceiling fans</li></ul>
  <ul class="abs cap-list" style="left:246px"><li>Exhaust fans</li><li>Kitchen / Bathroom Projects</li><li>Re-wires</li><li>Smart wiring</li><li>Phone points</li><li>Data points</li><li>Mains/sub mains cabling</li><li>Switchboard installations/relocations</li><li>Compliance investigations/inspections</li><li>Concrete and wall chasing</li><li>Temporary builders site power</li></ul>
  <ul class="abs cap-list" style="left:342px"><li>24hr Support / faults</li><li>Lighting/power design and consultation</li><li>Commercial lighting</li><li>Emergency and exit lighting</li><li>Led strip lighting</li><li>Energy efficient lighting</li><li>Temporary lighting</li><li>Illuminated signage</li><li>Switchboard relocations</li><li>Maintenance</li><li>RCD installation</li></ul>
  <ul class="abs cap-list" style="left:438px"><li>Phone/data points</li><li>Data cabinets</li><li>Data Networking</li><li>IDF installations/relocations</li><li>All power requirements</li><li>All three phase power requirements</li><li>Electrical rip outs / Disconnections</li><li>Thermal Imaging scans</li><li>Concrete and wall chasing</li><li>Retail lighting</li><li>Public building works</li></ul>
</section>

<section>
  <div class="abs contact"></div>
  <h2 class="abs section-title" style="top:902px">Contact Us</h2>
  <div class="abs field" style="left:151px;top:933px;width:183px">Name</div>
  <div class="abs field" style="left:340px;top:933px;width:183px">Email</div>
  <div class="abs field" style="left:151px;top:958px;width:183px">Phone number</div>
  <div class="abs field" style="left:340px;top:958px;width:112px">+ Add file......</div>
  <div class="abs btn-red" style="left:458px;top:958px;width:65px;height:16px;line-height:16px">Upload files</div>
  <div class="abs field" style="left:151px;top:984px;width:372px;height:58px;line-height:16px">Message</div>
  <div class="abs btn-red" style="left:151px;top:1053px;width:372px;height:15px;line-height:15px">Send</div>

  <div class="abs info" style="left:139px">
    <svg width="10" height="9" viewBox="0 0 10 9"><path d="M1 3.5C1 2 3 1 5 1s4 1 4 2.5H7V3H3v.5zM2.5 4h5L9 8H1z" fill="#e21f26"/></svg>
    <h4>Phone/Fax</h4><p>P: 0400 318 562<br>F: 08 9310 2284</p>
  </div>
  <div class="abs info" style="left:235px">
    <svg width="10" height="9" viewBox="0 0 10 9"><rect x=".5" y="1.5" width="9" height="6.5" fill="#e21f26"/><path d="M.5 1.5 5 5.5l4.5-4" fill="none" stroke="#222021" stroke-width=".8"/></svg>
    <h4>Email</h4><p>info@brightvaleelectrical.com.au</p>
  </div>
  <div class="abs info" style="left:329px">
    <svg width="10" height="9" viewBox="0 0 10 10"><circle cx="5" cy="5" r="4" fill="none" stroke="#e21f26" stroke-width="1.3"/><path d="M5 2.5V5h2" fill="none" stroke="#e21f26" stroke-width="1"/></svg>
    <h4>Link</h4><p>www.brightvaleelectrical.com.au</p>
  </div>
  <div class="abs info" style="left:424px">
    <svg width="10" height="10" viewBox="0 0 10 10"><path d="M5 .5C3 .5 1.8 2 1.8 3.8 1.8 6.3 5 9.5 5 9.5s3.2-3.2 3.2-5.7C8.2 2 7 .5 5 .5z" fill="#e21f26"/><circle cx="5" cy="3.8" r="1.2" fill="#222021"/></svg>
    <h4>Postal Address</h4><p>P.O Box 417 Seaview<br>W.A 6031</p>
  </div>
</section>

<footer>
  <div class="abs site-footer"><span class="abs" style="left:151px;top:13px">© Brightvale Electrical &amp; Communications.</span></div>
</footer>

</body>
</html>
```